" A empresa irá adquirir lotes e fazer a construção de casas para colocar a venda no mercado imobiliário norte americano, podendo captar uma parte do valor para investir de investidores que queiram um rendimento na economia real. "

```html
<!DOCTYPE html>
<html lang="pt-BR">
<head>
<meta charset="UTF-8">
<title>Assinatura de e-mail — Oakmere Builders</title>
<link rel="stylesheet" href="https://fonts.googleapis.com/css2?family=Montserrat:wght@400;600;700&display=swap">
<style>
  :root {
    --page: #ececec;
    --ink-dark: #1c1c1c;
    --teal: #3a97a8;
    --paper: #ffffff;
    --text: #2a2a2a;
    --faint: #ececec;
  }
  * { margin: 0; padding: 0; box-sizing: border-box; }
  html, body {
    width: 1200px; height: 1200px; overflow: hidden;
    background: var(--page);
    font-family: "Montserrat", sans-serif;
  }
  .signature {
    position: absolute; left: 84px; top: 492px;
    width: 1032px; height: 228px;
    background: var(--paper);
    display: flex;
  }
  .brand-panel {
    position: relative;
    width: 535px; height: 100%;
    background: var(--ink-dark);
    overflow: hidden;
  }
  .brand-panel__accent {
    position: absolute; left: 0; top: 0;
    width: 22px; height: 100%;
    background: var(--teal);
  }
  .brand-name {
    position: absolute; left: 0; right: 0; top: 50%;
    transform: translateY(-50%);
    display: flex; align-items: center; justify-content: center; gap: 14px;
  }
  .brand-name__mark {
    width: 30px; height: 30px; background: var(--teal);
  }
  .brand-name__text {
    color: var(--paper);
    font-weight: 600; font-size: 34px; letter-spacing: 3px;
  }
  .divider {
    position: absolute; left: 535px; top: 19px;
    width: 10px; height: 173px;
    background: var(--teal);
  }
  .contact {
    position: absolute; left: 574px; top: 28px;
    color: var(--text);
  }
  .contact__name {
    color: var(--teal); font-weight: 600; font-size: 26px; line-height: 1;
  }
  .contact__role {
    font-weight: 600; font-size: 13px; margin-top: 6px; text-transform: uppercase;
  }
  .contact__list { list-style: none; margin-top: 18px; }
  .contact__item {
    display: flex; align-items: center; gap: 14px;
    font-size: 12.5px; line-height: 1.35; margin-bottom: 10px;
  }
  .contact__item svg { width: 20px; height: 20px; flex: none; fill: var(--teal); }
  .contact__item strong { font-weight: 700; }
  .faint-block {
    position: absolute; right: 40px; top: 36px;
    width: 150px; height: 150px;
    background: var(--faint);
  }
</style>
</head>
<body>
  <section class="signature">
    <div class="brand-panel">
      <div class="brand-panel__accent"></div>
      <div class="brand-name">
        <span class="brand-name__mark"></span>
        <span class="brand-name__text">OAKMERE BUILDERS</span>
      </div>
    </div>
    <div class="divider"></div>
    <div class="faint-block"></div>
    <div class="contact">
      <h1 class="contact__name">NOME COMPLETO</h1>
      <p class="contact__role">Cargo ou função</p>
      <ul class="contact__list">
        <li class="contact__item">
          <svg viewBox="0 0 24 24" aria-hidden="true"><path d="M6.6 10.8a15 15 0 0 0 6.6 6.6l2.2-2.2a1 1 0 0 1 1-.25 11.4 11.4 0 0 0 3.6.57 1 1 0 0 1 1 1V20a1 1 0 0 1-1 1A17 17 0 0 1 3 4a1 1 0 0 1 1-1h3.5a1 1 0 0 1 1 1c0 1.25.2 2.45.57 3.57a1 1 0 0 1-.25 1z"/></svg>
          <span>00 0000.00000<br>00 0000.00000</span>
        </li>
        <li class="contact__item">
          <svg viewBox="0 0 24 24" aria-hidden="true"><path d="M12 2a10 10 0 1 0 0 20 10 10 0 0 0 0-20zm6.9 6h-2.9a15.7 15.7 0 0 0-1.4-3.6A8 8 0 0 1 18.9 8zM12 4c.8 1.2 1.5 2.5 1.9 4h-3.8c.4-1.5 1.1-2.8 1.9-4zM4.3 14a8 8 0 0 1 0-4h3.4a16.5 16.5 0 0 0 0 4zm.8 2h2.9c.3 1.3.8 2.5 1.4 3.6A8 8 0 0 1 5.1 16zM8 8H5.1a8 8 0 0 1 4.3-3.6C8.8 5.5 8.3 6.7 8 8zm4 12c-.8-1.2-1.5-2.5-1.9-4h3.8c-.4 1.5-1.1 2.8-1.9 4zm2.3-6H9.7a14.7 14.7 0 0 1 0-4h4.6a14.7 14.7 0 0 1 0 4zm.3 5.6c.6-1.1 1.1-2.3 1.4-3.6h2.9a8 8 0 0 1-4.3 3.6zm1.7-5.6a16.5 16.5 0 0 0 0-4h3.4a8 8 0 0 1 0 4z"/></svg>
          <span><strong>oakmerebuilders.com.br</strong><br><strong>contato@oakmerebuilders.com.br</strong></span>
        </li>
        <li class="contact__item">
          <svg viewBox="0 0 24 24" aria-hidden="true"><path d="M12 2a7 7 0 0 0-7 7c0 5.2 7 13 7 13s7-7.8 7-13a7 7 0 0 0-7-7zm0 9.5A2.5 2.5 0 1 1 12 6.5a2.5 2.5 0 0 1 0 5z"/></svg>
          <span>Nome da <strong>rua, 000</strong> - bairro<br><strong>cidade</strong> - estado - <strong>cep</strong> e país</span>
        </li>
      </ul>
    </div>
  </section>
</body>
</html>
```